Summer Sale Graphics for Social Media

I want to create 11 social media graphics (new Instagram size 4:5 (1080 x 1350 pixels) focusing on our Summer Sale Graphics, using any of the pics attached. Use the attached pics, NO RANDOM STOCK PHOTOGRAPHY. For the color scheme of the graphics, they should all be complementary to the product colors in the photos.
You can add any of the photos attached but none are required. You can do some of the graphics in all text. I mainly need BOLD text that says one of the headlines (11 total) SEE ATTACHED WORD DOCUMENT for the headlines to use.

```html
<!DOCTYPE html>
<html lang="en">
<head>
<meta charset="utf-8">
<title>Summer Sale Social Graphics</title>
<link rel="stylesheet" href="https://fonts.googleapis.com/css2?family=Poppins:wght@400;500;600;700;800&family=Libre+Baskerville&display=swap">
<style>
  :root {
    --tan: #b98a72;
    --brown: #6d4a3a;
    --brown-deep: #6b4436;
    --red: #e2282d;
    --ink: #232323;
    --charcoal: #333333;
    --slate: #555555;
    --mist: #f0f0f0;
    --white: #ffffff;
  }
  * { margin: 0; padding: 0; box-sizing: border-box; }
  html, body { width: 1200px; height: 1200px; overflow: hidden; background: var(--white); }
  body { position: relative; font-family: "Poppins", sans-serif; }
  .post {
    position: absolute; width: 419px; height: 523px; overflow: hidden;
    box-shadow: 0 0 10px rgba(0,0,0,0.08);
  }
  .post > * { position: absolute; line-height: 1; white-space: nowrap; }
  .handle {
    left: 0; width: 100%; top: 490px; text-align: center;
    font-family: "Libre Baskerville", serif; font-size: 13px; letter-spacing: 1.5px;
  }
  .tag { display: flex; align-items: center; justify-content: center; font-weight: 600; color: var(--white); }

  /* Post 1 */
  .post--waiting { left: 169px; top: 60px; background: var(--white); }
  .post--waiting .bands { left: 0; top: 0; width: 419px; height: 523px; }
  .post--waiting .title { left: 22px; top: 22px; font-size: 80px; font-weight: 700; color: var(--tan); letter-spacing: -1px; }
  .post--waiting .subtitle { left: 26px; top: 93px; font-size: 26px; font-weight: 500; letter-spacing: 5px; color: var(--ink); }
  .post--waiting .lead { left: 26px; top: 165px; font-size: 24px; font-weight: 500; color: var(--ink); }
  .post--waiting .you { left: 25px; top: 188px; font-size: 44px; font-weight: 500; color: var(--tan); }
  .post--waiting .sale { left: 25px; top: 255px; font-size: 62px; font-weight: 700; color: var(--brown-deep); }
  .post--waiting .now { left: 26px; top: 308px; font-size: 48px; font-weight: 600; letter-spacing: 6px; color: var(--ink); }
  .post--waiting .tag { left: 27px; top: 355px; width: 151px; height: 29px; background: var(--tan); font-size: 19px; }
  .post--waiting .photo {
    left: 200px; top: 134px; width: 212px; height: 389px;
    border-radius: 90px 90px 0 0;
    background: linear-gradient(180deg, #3a2a24 0%, #8a5e4a 35%, #8a5e4a 62%, #1d1a1a 82%, #151313 100%);
  }
  .post--waiting .handle { color: var(--white); }

  /* Post 2 */
  .post--one-body { left: 620px; top: 60px; background: var(--white); }
  .post--one-body .one-box { left: 30px; top: 114px; width: 91px; height: 208px; background: var(--red); }
  .post--one-body .one {
    left: 75px; top: 218px; font-size: 86px; font-weight: 700; color: var(--white);
    transform: translate(-50%, -50%) rotate(-90deg); letter-spacing: -1px;
  }
  .post--one-body .sale { left: 126px; top: 98px; font-size: 113px; font-weight: 700; color: var(--red); letter-spacing: -6px; }
  .post--one-body .body { left: 127px; top: 192px; font-size: 92px; font-weight: 700; color: var(--slate); letter-spacing: -1px; }
  .post--one-body .summer { left: 127px; top: 271px; font-size: 58px; font-weight: 700; color: var(--slate); letter-spacing: -1px; }
  .post--one-body .tag { left: 30px; top: 334px; width: 193px; height: 38px; background: var(--red); font-size: 25px; }
  .post--one-body .slay { left: 235px; top: 327px; font-size: 30px; font-weight: 400; letter-spacing: 5.5px; color: var(--ink); }
  .post--one-body .handle { color: var(--slate); }

  /* Post 3 */
  .post--slim-waist { left: 169px; top: 624px; background: var(--mist); }
  .post--slim-waist .line { left: 34px; font-size: 58px; font-weight: 700; color: var(--charcoal); letter-spacing: -0.5px; }
  .post--slim-waist .line-1 { top: 20px; }
  .post--slim-waist .line-2 { top: 70px; }
  .post--slim-waist .line-3 { top: 118px; font-size: 51px; color: var(--red); letter-spacing: -1px; }
  .post--slim-waist .products {
    left: 40px; top: 179px; width: 341px; height: 182px; border-radius: 14px 14px 8px 8px;
    background: linear-gradient(90deg, #e9ecf4 0%, #f8f8f8 30%, #fbeeee 55%, #f4e8f1 80%, #ece4ee 100%);
  }
  .post--slim-waist .go { left: 40px; top: 363px; font-size: 20px; font-weight: 600; color: var(--charcoal); }
  .post--slim-waist .sale { left: 38px; top: 381px; font-size: 62px; font-weight: 700; color: var(--red); letter-spacing: -1px; }
  .post--slim-waist .tag { left: 133px; top: 442px; width: 151px; height: 29px; background: var(--charcoal); font-size: 19px; }
  .post--slim-waist .handle { color: var(--slate); }

  /* Post 4 */
  .post--slim-down { left: 620px; top: 624px; background: var(--white); }
  .post--slim-down .center { left: 0; width: 100%; text-align: center; }
  .post--slim-down .hurry { top: 41px; font-size: 52px; font-weight: 700; color: var(--red); }
  .post--slim-down .our { left: 54px; top: 129px; font-size: 29px; font-weight: 500; letter-spacing: 13.5px; color: var(--ink); }
  .post--slim-down .slim { left: 52px; top: 153px; font-size: 54px; font-weight: 700; color: var(--ink); letter-spacing: -1px; }
  .post--slim-down .sale { left: 48px; top: 188px; font-size: 134px; font-weight: 800; color: var(--red); letter-spacing: -6px; }
  .post--slim-down .is-on { right: 55px; top: 302px; font-size: 26px; font-weight: 600; color: var(--ink); }
  .post--slim-down .miss { top: 364px; font-size: 48px; font-weight: 700; color: var(--red); letter-spacing: -1px; }
  .post--slim-down .tag { left: 133px; top: 416px; width: 151px; height: 28px; background: var(--charcoal); font-size: 19px; }
  .post--slim-down .handle { color: var(--slate); }
</style>
</head>
<body>

<section class="post post--waiting">
  <svg class="bands" viewBox="0 0 419 523" aria-hidden="true">
    <path d="M0 406 Q230 280 419 104 L419 523 L0 523 Z" fill="var(--tan)"/>
    <path d="M0 408 Q220 305 419 209 L419 523 L0 523 Z" fill="var(--brown)"/>
  </svg>
  <div class="title">SUMMER</div>
  <div class="subtitle">ISN’T WAITING</div>
  <div class="lead">Neither Should</div>
  <div class="you">YOU</div>
  <div class="sale">SALE</div>
  <div class="now">NOW!</div>
  <div class="tag">Up to $15 OFF</div>
  <div class="photo" role="img" aria-label="Smiling woman in a brown mesh top holding three supplement bottles"></div>
  <div class="handle">@BRIGHTLEAFDAILY</div>
</section>

<section class="post post--one-body">
  <div class="one-box"></div>
  <div class="one">ONE</div>
  <div class="sale">SALE</div>
  <div class="body">BODY</div>
  <div class="summer">SUMMER</div>
  <div class="tag">Up to $15 OFF</div>
  <div class="slay">TO SLAY</div>
  <div class="handle">@BRIGHTLEAFDAILY</div>
</section>

<section class="post post--slim-waist">
  <div class="line line-1">SLIM WAIST</div>
  <div class="line line-2">FLAT TUMMY</div>
  <div class="line line-3">MORE ENERGY</div>
  <div class="products" role="img" aria-label="Row of four white supplement bottles with blue, green, red and pink labels"></div>
  <div class="go">Let’s Go!</div>
  <div class="sale">SALE NOW !</div>
  <div class="tag">Up to $15 OFF</div>
  <div class="handle">@BRIGHTLEAFDAILY</div>
</section>

<section class="post post--slim-down">
  <div class="hurry center">HURRY!</div>
  <div class="our">OUR SUMMER</div>
  <div class="slim">SLIM-DOWN</div>
  <div class="sale">SALE</div>
  <div class="is-on">Is On</div>
  <div class="miss center">DON’T MISS IT!</div>
  <div class="tag">Up to $15 OFF</div>
  <div class="handle">@BRIGHTLEAFDAILY</div>
</section>

</body>
</html>
```